Business card and stationary for consulting business

We need business cards and matching stationary for professional consulting business for employment and human resources issues.
One of the CraftHive designers designed the logo with our company name.  Use the colors in the logo and may use light yellow as an accent color.
Add
Mara T. Vollen, J.D., LL.M.
485 E. Callister Lane
Winter Park, Florida  32789
407-555-0183
maravollenjd@quillpost.example

Industry/Entity Type
Business

```html
<!DOCTYPE html>
<html lang="en">
<head>
<meta charset="utf-8">
<title>Northfield Business Card</title>
<link rel="stylesheet" href="https://fonts.googleapis.com/css2?family=Roboto+Slab:wght@300;500&display=swap">
<style>
  :root {
    --backdrop: #ecebe7;
    --card: #ffffff;
    --brand-blue: #2a8fc4;
    --bar-blue: #3aa3e0;
    --accent-yellow: #f2e21a;
    --ink: #4a4a4a;
  }
  * { box-sizing: border-box; margin: 0; padding: 0; }
  html, body {
    width: 1200px; height: 899px; overflow: hidden;
    background: var(--backdrop);
  }
  .stage {
    position: relative; width: 1200px; height: 899px;
    display: flex; align-items: center; justify-content: center; gap: 40px;
  }
  .card {
    position: relative; width: 540px; height: 309px;
    background: var(--card);
    box-shadow: 0 2px 10px rgba(0,0,0,0.12);
    overflow: hidden;
    font-family: "Roboto Slab", serif;
  }
  .bar { position: absolute; }
  .bar--blue { background: var(--bar-blue); width: 62px; height: 14px; }
  .bar--yellow { background: var(--accent-yellow); width: 22px; height: 48px; left: 0; }

  .brand-name {
    position: absolute;
    font-family: "Roboto Slab", serif; font-weight: 500;
    color: var(--brand-blue); letter-spacing: 0.5px; white-space: nowrap;
  }

  /* back of card */
  .card--back .bar--blue { right: 70px; top: 0; }
  .card--back .bar--yellow { bottom: 60px; }
  .card--back .brand-name {
    left: 50%; top: 50%; transform: translate(-50%, -50%); font-size: 28px;
  }

  /* front of card */
  .card--front .bar--yellow { bottom: 40px; }
  .card--front .brand-name { left: 46px; top: 112px; font-size: 22px; }
  .holder {
    position: absolute; left: 236px; top: 112px;
    font-weight: 300; color: var(--ink); font-size: 17px; letter-spacing: 0.6px;
    white-space: nowrap;
  }
  .address, .contact {
    position: absolute; bottom: 36px;
    font-weight: 300; color: var(--ink); font-style: normal; line-height: 1.45;
    white-space: nowrap;
  }
  .address { left: 46px; font-size: 15px; }
  .contact { right: 28px; text-align: right; font-size: 14px; }
</style>
</head>
<body>
<main class="stage">
  <section class="card card--back" aria-label="Card back">
    <span class="bar bar--blue"></span>
    <span class="bar bar--yellow"></span>
    <span class="brand-name">Northfield</span>
  </section>

  <section class="card card--front" aria-label="Card front">
    <span class="bar bar--yellow"></span>
    <span class="brand-name">Northfield</span>
    <p class="holder">Mara T. Vollen, J.D., LL.M.</p>
    <address class="address">
      485 E. Callister Lane<br>
      Alder Springs, Florida 32990
    </address>
    <p class="contact">
      407-555-0183<br>
      maravollenjd@quillpost.example
    </p>
  </section>
</main>
</body>
</html>
```